Simple but elegant business card/logo design for exclusive beauty business

We need a logo designed for a new elegant and exclusive beauty business called "G". The logo itself should be a stylistic and custom design for the letter "G". We would like the business card to have the logo as the centrepiece on a clean background. Gold Logo on black background or silver on white background.

The business card details should be displayed centre of the card. Details are as follows:

Tamsin Rowe
Chatterly: /simplyshinebyr
Picturo: /simplyshinebyr

The words "Simply Shine" should also appear somewhere on the card.

G

• Design must be simple, clean and elegant
• The design should not be cluttered

```html
<!DOCTYPE html>
<html lang="en">
<head>
<meta charset="utf-8">
<title>Tamsin Rowe – Business Card</title>
<link rel="stylesheet" href="https://fonts.googleapis.com/css2?family=Michroma&family=Orbitron:wght@500&family=Tinos&display=swap">
<style>
  :root {
    --backdrop: #ececec;
    --card: #1c1d27;
    --card-edge: #14151d;
    --gold: #f1df7a;
    --gold-deep: #c9a93c;
    --gold-glow: rgba(255, 230, 120, 0.45);
  }
  * { margin: 0; padding: 0; box-sizing: border-box; }
  html, body {
    width: 1200px;
    height: 676px;
    overflow: hidden;
    background: var(--backdrop);
  }
  .canvas {
    width: 1200px;
    height: 676px;
    display: flex;
    align-items: center;
    justify-content: center;
    gap: 40px;
  }
  .card {
    width: 540px;
    height: 309px;
    background: linear-gradient(160deg, #23242f 0%, var(--card) 55%, var(--card-edge) 100%);
    box-shadow: 0 8px 24px rgba(0, 0, 0, 0.25);
    display: flex;
    flex-direction: column;
    align-items: center;
    justify-content: center;
  }
  .brand-mark {
    display: flex;
    align-items: center;
    gap: 18px;
    margin-bottom: 36px;
  }
  .brand-mark__disc {
    width: 62px;
    height: 62px;
    border-radius: 50%;
    background: radial-gradient(circle at 35% 35%, var(--gold) 0%, var(--gold-deep) 70%);
  }
  .brand-mark__name {
    font-family: "Tinos", serif;
    font-size: 58px;
    line-height: 1;
    color: var(--gold);
  }
  .holder-name {
    font-family: "Michroma", sans-serif;
    font-weight: 400;
    font-size: 30px;
    letter-spacing: 5px;
    color: var(--gold);
    text-shadow: 0 0 6px var(--gold-glow);
  }
  .tagline {
    font-family: "Orbitron", sans-serif;
    font-weight: 500;
    font-size: 46px;
    letter-spacing: 2px;
    color: var(--gold);
    text-shadow: 0 0 8px var(--gold-glow);
    margin-bottom: 40px;
  }
  .socials {
    display: flex;
    gap: 30px;
  }
  .social {
    display: flex;
    align-items: center;
    gap: 8px;
    font-family: "Tinos", serif;
    font-size: 18px;
    color: var(--gold);
    text-shadow: 0 0 5px var(--gold-glow);
  }
  .social__network {
    font-size: 13px;
    letter-spacing: 1px;
    text-transform: uppercase;
    color: var(--gold-deep);
    text-shadow: none;
  }
  .social__icon {
    width: 20px;
    height: 20px;
    background: var(--gold-deep);
  }
  .social__icon--circle { border-radius: 50%; }
  .social__icon--square { border-radius: 3px; }
</style>
</head>
<body>
  <main class="canvas">
    <section class="card card--front">
      <div class="brand-mark">
        <span class="brand-mark__disc"></span>
        <span class="brand-mark__name">Rowe Atelier</span>
      </div>
      <h1 class="holder-name">Tamsin Rowe</h1>
    </section>

    <section class="card card--back">
      <p class="tagline">Simply Shine</p>
      <div class="socials">
        <span class="social">
          <span class="social__icon social__icon--circle"></span>
          <span class="social__network">Chatterly</span>
          /simplyshinebyr
        </span>
        <span class="social">
          <span class="social__icon social__icon--square"></span>
          <span class="social__network">Picturo</span>
          /simplyshinebyr
        </span>
      </div>
    </section>
  </main>
</body>
</html>
```